Stationary/business card/envelope design for Larkvale Dentalcare

We are located in the foothills of the sierra nevada mountains. We are looking for a beautiful classy modern stationary. We need evelopes and business card design all to flow seamlessly. Envelope design.

Additional office address 4816 Meridian Wy., Suite B, Auburn, CA 95604 Phone: pending Fax: pending.

3 different Drs on each business card:
Helen R. Marsh, DDS
Orla P. Marsh, DDS
Rebecca S. Halvey, DDS

Target Market(s)

Dental patients

Industry/Entity Type

Dental

Contact Information for Business Card

Two sided. See example.

Font styles to use
Sans Serif

Requirements
Must have
• One sided business cards. Need envelope design.
Colors should match existing logo.

Helen R. Marsh, DDS
Orla P. Marsh, DDS
Rebecca S. Halvey, DDS

```html
<!DOCTYPE html>
<html lang="en">
<head>
<meta charset="utf-8">
<title>Larkvale Dentalcare – Business Card</title>
<link rel="stylesheet" href="https://fonts.googleapis.com/css2?family=Questrial&family=Tinos&display=swap">
<style>
  :root {
    --backdrop: #b1b1ad;
    --card-white: #ffffff;
    --card-dark: #2a2a2b;
    --edge-blue: #3bb3de;
    --brand-green: #2a7a3a;
    --text-grey: #555555;
    --icon-green: #2f7d3c;
  }
  * { margin: 0; padding: 0; box-sizing: border-box; }
  html, body { width: 1200px; height: 801px; overflow: hidden; }
  body {
    background: var(--backdrop);
    display: flex;
    align-items: center;
    justify-content: center;
    gap: 48px;
  }
  .card {
    width: 530px;
    height: 303px;
    position: relative;
    border-bottom: 6px solid var(--edge-blue);
    box-shadow: 0 10px 24px rgba(0,0,0,0.25);
  }
  .card--front { background: var(--card-white); }
  .card--back { background: var(--card-dark); display: flex; align-items: center; justify-content: center; }

  .doctor { position: absolute; left: 34px; top: 40px; font-family: "Tinos", serif; }
  .doctor__name { color: var(--brand-green); font-size: 22px; letter-spacing: 0.5px; text-transform: uppercase; font-weight: 400; }
  .doctor__title { color: var(--text-grey); font-size: 14px; margin-top: 2px; }

  .brand { font-family: "Questrial", sans-serif; color: var(--brand-green); display: flex; align-items: center; gap: 12px; }
  .brand__dot { width: 22px; height: 22px; border-radius: 50%; background: var(--edge-blue); flex: none; }
  .brand__name { font-size: 24px; line-height: 1.15; letter-spacing: 2px; }
  .card--front .brand { position: absolute; right: 30px; top: 100px; }

  .contact { position: absolute; left: 34px; bottom: 30px; font-family: "Tinos", serif; color: var(--text-grey); font-size: 14px; line-height: 1.35; list-style: none; }
  .contact__address { margin-bottom: 8px; }
  .contact li { display: flex; align-items: center; gap: 8px; }
  .contact svg { width: 11px; height: 11px; fill: var(--icon-green); flex: none; }
</style>
</head>
<body>
  <section class="card card--front">
    <div class="doctor">
      <h1 class="doctor__name">Rebecca S. Halvey, DDS</h1>
      <p class="doctor__title">Family &amp; Cosmetic Dentistry</p>
    </div>

    <div class="brand">
      <span class="brand__dot"></span>
      <span class="brand__name">Larkvale<br>Dental Care<br>Corporation</span>
    </div>

    <ul class="contact">
      <li class="contact__address">4816 Meridian Wy.,<br>Suite B, Auburn, CA 95604</li>
      <li><svg viewBox="0 0 12 12"><path d="M2.5 1h2l1 3-1.3 1a6 6 0 0 0 2.8 2.8l1-1.3 3 1v2c0 .6-.4 1-1 1A9.5 9.5 0 0 1 1.5 2c0-.6.4-1 1-1z"/></svg>(530) 555-0142</li>
      <li><svg viewBox="0 0 12 12"><rect x="1" y="4" width="10" height="6" rx="1"/><rect x="3" y="1" width="6" height="3"/></svg>(530) 555-0186</li>
      <li><svg viewBox="0 0 12 12"><path d="M1 2.5h10v7H1z M1 2.5l5 4 5-4" fill="none" stroke="#2f7d3c" stroke-width="1.2"/></svg>larkvaledentalcare@mailbox.net</li>
      <li><svg viewBox="0 0 12 12"><circle cx="6" cy="6" r="5" fill="none" stroke="#2f7d3c" stroke-width="1.1"/><path d="M1 6h10M6 1c-2.5 3-2.5 7 0 10M6 1c2.5 3 2.5 7 0 10" fill="none" stroke="#2f7d3c" stroke-width="0.9"/></svg>www.larkvaledentalcare.com</li>
    </ul>
  </section>

  <section class="card card--back">
    <div class="brand">
      <span class="brand__dot"></span>
      <span class="brand__name">Larkvale<br>Dental Care<br>Corporation</span>
    </div>
  </section>
</body>
</html>
```